Zappo! Dog Training & Boarding School

I need a brochure that makes people aware of the dog training services I offer. This includes:
Group Classes
Private lessons
Help with Behavior Problems
Boarding School
.See my website: www.zappodogtraining.com

Target Market(s)

People with dogs

Industry/Entity Type

School

Font styles to use
Serif

Requirements
Must have
• My Logo and Tag line. Must be trifold brochure. Include brief description of services and training philosophy, a little info about me and some important lines from testimonials. I like bright colors, pics of happy dogs and happy people.
Nice to have
• I thought it would be cool to have something on the cover where there are people seeming saying "What do want? Well mannered dogs! How do we get them? Zappo! Dog Training" Then a group of dogs saying "What do we want? People we understand! How do we get them? Zappo! Dog Training"

```html
<!DOCTYPE html>
<html lang="en">
<head>
<meta charset="utf-8">
<title>Zappo! Dog Training – Brochure Inside</title>
<link href="https://fonts.googleapis.com/css2?family=Archivo:wght@700;800&family=Playfair+Display:ital,wght@1,700;1,800&family=Questrial&display=swap" rel="stylesheet">
<style>
  :root{
    --page-bg:#d3d4d4;
    --panel-cream:#f6f5df;
    --panel-mint:#eef1da;
    --ink:#4b4b4b;
    --blue:#2b4aa3;
    --red:#e2212b;
    --rule:#27394a;
    --paw:#b3b8ad;
    --bullet:#9aa63a;
  }
  *{box-sizing:border-box;margin:0;padding:0}
  html,body{width:1200px;height:900px;overflow:hidden;background:var(--page-bg)}
  .brochure{position:absolute;left:101px;top:62px;width:1000px;height:771px;display:flex;overflow:hidden}
  .panel{position:relative;height:100%}
  .panel--left{width:331px;background:var(--panel-cream)}
  .panel--middle{width:335px;background:var(--panel-mint)}
  .panel--right{width:334px;background:var(--panel-cream)}
  .photo{position:absolute}
  .paw{position:absolute;width:62px;height:70px}
  .body-copy{font-family:"Questrial",sans-serif;font-size:14.2px;line-height:17.6px;color:var(--ink)}
  .body-copy p{text-indent:8px;margin-bottom:7px}

  /* left panel */
  .headline{position:absolute;left:0;width:331px;top:236px;text-align:center}
  .headline .sans{display:block;font-family:"Archivo",sans-serif;font-weight:800;font-size:27px;line-height:28px;color:var(--blue)}
  .headline .accent{display:block;font-family:"Playfair Display",serif;font-style:italic;font-weight:800;font-size:40px;line-height:36px;color:var(--red)}
  .panel--left .body-copy{position:absolute;left:24px;top:327px;width:290px}

  /* middle panel */
  .panel--middle .body-copy{position:absolute;left:27px;top:2px;width:290px}

  /* right panel */
  .quote-mark{position:absolute;left:98px;top:20px;width:140px;height:44px}
  .testimonial-lead{position:absolute;left:28px;top:68px;width:285px;font-family:"Playfair Display",serif;font-style:italic;font-weight:700;font-size:15.6px;line-height:19px;color:var(--red)}
  .panel--right .body-copy{position:absolute;left:26px;top:207px;width:288px}
  .signature{text-align:right;text-indent:0!important}
  .rule{position:absolute;left:26px;width:283px;height:2px;background:var(--rule)}
  .why-train{position:absolute;left:26px;top:551px;font-family:"Archivo",sans-serif;font-weight:800;font-size:24px;line-height:26px;color:var(--blue)}
  .why-train .accent{font-family:"Playfair Display",serif;font-style:italic;font-size:34px;color:var(--red);margin-left:4px}
  .benefits{position:absolute;left:26px;top:620px;width:290px;list-style:none;font-family:"Questrial",sans-serif;font-size:16px;line-height:19px;color:#333}
  .benefits li{position:relative;padding-left:24px;margin-bottom:7px}
  .benefits li::before{content:"";position:absolute;left:2px;top:3px;width:11px;height:11px;border-radius:50%;background:var(--bullet)}
</style>
</head>
<body>
<main class="brochure">

  <section class="panel panel--left">
    <div class="photo" role="img" aria-label="Photo of several dogs relaxing together on a porch" style="left:0;top:0;width:198px;height:225px;background:linear-gradient(160deg,#b9a88a,#6a5a48 55%,#4d8a4f)"></div>
    <div class="photo" role="img" aria-label="Photo of a collie on grass" style="left:204px;top:0;width:131px;height:66px;background:linear-gradient(160deg,#6f9a49,#b48a4e)"></div>
    <div class="photo" role="img" aria-label="Photo of dogs on a sandy beach" style="left:204px;top:70px;width:131px;height:76px;background:linear-gradient(170deg,#8aa3b5,#b9a58a)"></div>
    <div class="photo" role="img" aria-label="Close-up photo of a happy shaggy dog" style="left:204px;top:150px;width:131px;height:75px;background:linear-gradient(150deg,#6d8d4a,#a38d78)"></div>

    <h1 class="headline">
      <span class="sans">Why positive</span>
      <span class="accent">reinforcement</span>
      <span class="sans">works</span>
    </h1>

    <svg class="paw" role="img" aria-label="Paw print decoration" style="left:287px;top:314px" viewBox="0 0 62 70"><ellipse cx="31" cy="40" rx="24" ry="26" fill="var(--paw)" opacity=".8"/></svg>

    <div class="body-copy">
      <p>Because it is grounded in the science of how dogs learn and anyone can do it.</p>
      <p>With Positive Reinforcement training, we teach dogs manners and the meaning of words or hand-signals using a reward-based system. When a dog does something we like, we give that dog something they like – food, toys, belly rubs, play, praise, etc. Dogs, being the clever companions they are, quickly learn which behaviors get rewarded and repeat those behaviors in the future.</p>
      <p>Because the use of Positive Reinforcement is so encouraging and gentle, it builds a dogs trust and confidence. This aspect is extremely important because the primary cause of behavior problems in dogs is anxiety. By choosing to use Positive Reinforcement training methods whenever possible, we can greatly diminish the chance of our dogs developing behavior problems.</p>
      <p>What I like most about PR training is how fun it is for the dogs AND the people - even children can participate in the process!</p>
    </div>
  </section>

  <section class="panel panel--middle">
    <svg class="paw" role="img" aria-label="Paw print decoration" style="left:290px;top:50px" viewBox="0 0 62 70"><ellipse cx="31" cy="40" rx="24" ry="26" fill="var(--paw)" opacity=".8"/></svg>
    <div class="body-copy">
      <p>Most dog behaviors we “parents” find inappropriate aren't intended to be a challenge to our authority — they're just natural dog behaviors. After all, dogs just want to have fun, be part of the family, and have some purpose – they're not conspiring to take over the throne! And they don't always know that those chewable-looking shoes aren't toys ;)</p>
      <p>Just because this family member is a different species doesn't mean you need to let confusion and havoc prevail. My training will let you move beyond just saying NO! all the time — it will show you how to provide your dog with information about what's right.</p>
      <p>My training methods (link to PRT page) work on all breeds and types of dogs, because they are well-grounded in the science of how animals learn. And, I'm the solo trainer at Zappo!, so you can be sure that your dog will get the very best in professional training. (link to about page)</p>
      <p>I teach my clients how to better understand their dog and how to communicate in a meaningful way — and my training (link to PRT page) works.</p>
    </div>
    <div class="photo" role="img" aria-label="Photo of two black and white dogs lying on a beach" style="left:26px;top:498px;width:290px;height:98px;background:linear-gradient(180deg,#c9b9a0,#e6dccb)"></div>
    <div class="photo" role="img" aria-label="Photo of a small dog sitting on a chair" style="left:26px;top:602px;width:119px;height:91px;background:linear-gradient(160deg,#c7a57e,#8d7660)"></div>
    <div class="photo" role="img" aria-label="Close-up photo of a scruffy terrier" style="left:26px;top:698px;width:119px;height:73px;background:linear-gradient(160deg,#9b7f67,#d4c3a8)"></div>
    <div class="photo" role="img" aria-label="Photo of dogs resting on a lawn in front of a yellow house" style="left:151px;top:602px;width:165px;height:169px;background:linear-gradient(180deg,#7fb0de 0%,#c8a53a 38%,#5e9a3c 62%,#4f8d35)"></div>
  </section>

  <section class="panel panel--right">
    <svg class="quote-mark" viewBox="0 0 140 44" aria-hidden="true">
      <line x1="0" y1="22" x2="36" y2="22" stroke="var(--blue)" stroke-width="2"/>
      <line x1="104" y1="22" x2="140" y2="22" stroke="var(--blue)" stroke-width="2"/>
      <circle cx="70" cy="22" r="21" fill="var(--blue)"/>
      <text x="70" y="36" text-anchor="middle" font-family="Playfair Display, serif" font-weight="700" font-size="30" fill="#fff">“</text>
    </svg>
    <p class="testimonial-lead">I had a wonderful experience with Marissa, and I'm looking forward to working with her again! Marissa demonstrates the skills needed to be a great teacher - communication, clarity of content delivery, and patience. Being a teacher myself,.</p>
    <div class="body-copy">
      <p>I was very pleased with the way Marissa structured and provided her class with a detailed timeline of what content was going to be covered when, a manual which provided thorough detail of each skill covered, and "homework" - a packet with a weekly checklist of what skills to practice at home before the next week.All of these resources, when actually used by the student, does create a positive learning experience. Marissa was very quick to respond to my emails, and she was very understanding of my position of a frustrated and discouraged owner. She was always very encouraging and honest with me in a very graceful manner.</p>
      <p style="margin-top:17px">Thank you Marissa! You'll be seeing me and Pepper again soon!</p>
      <p class="signature">~Dalia</p>
    </div>
    <div class="rule" style="top:543px"></div>
    <h2 class="why-train">Why<span class="accent">train</span><br>with Zappo!</h2>
    <svg class="paw" role="img" aria-label="Paw print decoration" style="left:256px;top:554px" viewBox="0 0 62 70"><ellipse cx="31" cy="40" rx="24" ry="26" fill="var(--paw)" opacity=".8"/></svg>
    <ul class="benefits">
      <li>Work with an expert dog trainer</li>
      <li>Flexible training options</li>
      <li>Fast results</li>
      <li>Carefully tailored to meet your goals</li>
    </ul>
    <div class="rule" style="top:747px"></div>
  </section>

</main>
</body>
</html>
```